Mentorvale needs a WordPress - Design

I am a personal, team and business coach and help my clients to develop their potential. I mainly work with individuals and teams, but this can also be in the context of a company.
My business is called "Mentorvale"

The main goal of this website is to promote my business and to attire new customers.
I also want to present my concepts and ideas about coaching and how I actually do coaching and consulting. This is also to inform potential customers what coaching actually is and what it's not.
I want to host this website on a hosting-provider and want to be able to add and adapt content on my own. I'm thus looking for a WordPress - design.

Content:

vision
• Why do I do this
• How do I do this
• What am I doing

Coaching
• Career development
• Conflicts
• What is coaching, why coaching
• Conduct of a session and of the whole consultation
Limits of coaching
• Examples of positive effects of coaching

Support concept

Blog about current topics

Left

About me

Contact form

Footer / disclaimer

The following topics are the most important parts of my daily work as a coach with my clients, maybe this helps to get choos a suitable design:
- personality development, analyzing aspects and patterns and showing their influence
- Improve collaboration and cooperation in teams
- Addressing and solving conflicts (private and business)
- Identify and foster motivation, drivers, goals and action patterns
- Define next steps for the further improvement
- Accompany reorientation in professional career
- Discovering and using the strengths of the customers

The major part of my work is direct conversation with the customer, on site or virtually. My job is to support the customer in recognizing his own ideas, goals and possibilities and to define next steps in the desired direction

Target Market(s)

Small businesses and private persons in serch of a professional coach

Industry/Entity Type

Consultant

Number of Pages Required

1 page

Font styles to use
Sans Serif

Requirements
Must have
• - Logo / Name (see attachment)
- Menu, fixed navigation
- content
- blog
- Footer (contact, disclaimer)

- I need a WordPress design suitable for Mobile and Desktop devices.
- I'm looking for a modern, friendly and easy to use web site.
- First page as Long-pager (scrolling), other pages as long-pager or standard
- Decent, friendly colors but still clear, simple
Nice to have
• - Panorama image (image changing on every load of the site)
- Quote (changing on every load of the site)

```html
<!DOCTYPE html>
<html lang="en">
<head>
<meta charset="utf-8">
<title>Mentorvale — Coaching</title>
<link href="https://fonts.googleapis.com/css2?family=Mulish:wght@300;400;600;700;800&display=swap" rel="stylesheet">
<style>
:root{
  --navy:#262080;
  --navy-deep:#1b1960;
  --ink:#0f0c48;
  --sky:#1ea7e1;
  --sky-2:#1e8fd8;
  --text:#444a5a;
  --muted:#8a8f9c;
  --line:#d9dbe3;
  --mist:#e8ecf7;
  --white:#ffffff;
}
*{box-sizing:border-box;margin:0;padding:0}
html,body{width:1200px;height:4800px;overflow:hidden}
body{font-family:"Mulish",Arial,sans-serif;color:var(--text);background:var(--white);position:relative}
section,header,footer{position:relative;width:1200px;overflow:hidden}
.abs{position:absolute}
.h2{font-size:40px;font-weight:800;color:var(--navy);letter-spacing:.5px;text-transform:uppercase}
.btn{display:inline-block;background:var(--sky);color:#fff;font-size:15px;font-weight:600;text-transform:uppercase;height:40px;line-height:40px;padding:0 16px}

/* header */
.site-header{height:134px}
.brand{left:143px;top:22px;display:flex;flex-direction:column;align-items:flex-start}
.brand-mark{width:52px;height:52px;background:var(--sky);margin-left:38px;margin-bottom:10px}
.brand-name{font-size:15px;font-weight:600;color:var(--navy);letter-spacing:4px;text-transform:uppercase}
.header-phone{right:144px;top:34px;font-size:24px;font-weight:700;color:var(--navy);display:flex;align-items:center;gap:8px}
.main-nav{left:382px;right:144px;top:100px;display:flex;justify-content:space-between;font-size:13px;font-weight:600;color:#333;text-transform:uppercase}
.main-nav .is-active{color:var(--sky)}

/* hero */
.hero{height:480px}
.hero-photo{inset:0;background:linear-gradient(100deg,#3b4450 0%,#6e7680 35%,#9aa2aa 65%,#6d757d 100%)}
.hero-copy{right:144px;top:172px;text-align:right}
.hero-title{font-size:32px;font-weight:800;color:#fff;line-height:40px;text-transform:uppercase;text-shadow:0 2px 6px rgba(0,0,0,.35)}
.hero-cta{margin-top:10px;display:inline-block;background:var(--navy);color:#fff;font-size:15px;font-weight:600;height:43px;line-height:43px;padding:0 18px;text-transform:uppercase}
.slider-arrow{top:353px;width:44px;height:44px;border-radius:50%;background:#fff;display:flex;align-items:center;justify-content:center}

/* vision */
.vision{height:463px}
.vision .h2{left:143px;top:70px}
.vision-rule{left:143px;top:136px;width:914px;height:1px;background:var(--line)}
.vision-rule-active{left:143px;top:134px;width:241px;height:4px;background:var(--navy)}
.vision-split{left:384px;top:136px;width:1px;height:248px;background:var(--line)}
.vision-tabs{left:143px;top:136px;width:241px}
.vision-tab{height:80px;line-height:80px;font-size:24px;font-weight:300;color:#666;text-transform:uppercase;border-bottom:1px solid var(--line)}
.vision-tab:last-child{border-bottom:0}
.vision-tab.is-active{color:var(--sky)}
.vision-text{left:420px;top:160px;width:636px;font-size:13px;line-height:29px}
.vision-more{left:420px;top:335px}

/* coaching */
.coaching{height:557px;background:linear-gradient(90deg,#261f82 0%,#232890 45%,#1e8fd8 100%)}
.tile-grid{left:143px;top:80px;display:grid;grid-template-columns:repeat(3,298px);grid-auto-rows:193px;gap:10px}
.tile{background:#fff;display:flex;flex-direction:column;align-items:center;justify-content:center;text-align:center;padding:0 22px;font-size:15px;font-weight:600;color:#222;line-height:24px}
.tile svg{margin-bottom:14px}
.tile.tile-title{background:var(--navy-deep);color:#fff;font-size:40px;font-weight:800;text-transform:uppercase}

/* support */
.support{height:602px}
.support .h2{left:143px;top:143px}
.support-text{left:143px;top:205px;width:420px;font-size:14px;line-height:29px}
.support-btn{left:143px;top:398px}
.support-art{left:624px;top:80px;width:432px;height:435px;background:linear-gradient(135deg,#2cb4ea 0%,#1e8fd8 50%,#262080 100%)}

/* blog */
.blog{height:760px;background:var(--mist)}
.blog .h2{left:0;right:0;top:72px;text-align:center}
.blog-photo{left:143px;top:152px;width:441px;height:448px;background:linear-gradient(160deg,#8d99a6 0%,#5c6774 50%,#a6adb4 100%)}
.post{left:616px;width:440px;height:216px;background:#fff;box-shadow:0 2px 8px rgba(20,20,80,.08);padding:24px 22px}
.post-date{display:flex;align-items:flex-start;gap:16px}
.post-day{color:var(--sky);font-size:36px;font-weight:600;line-height:36px;padding-right:14px;border-right:1px solid var(--line);text-align:center}
.post-day span{display:block;font-size:22px;line-height:26px}
.post-meta{font-size:11px;line-height:20px;color:var(--muted);padding-top:10px}
.post-title{margin-top:16px;font-size:18px;font-weight:600;line-height:30px;color:var(--navy)}
.blog-btn{left:535px;top:634px;width:130px;text-align:center}

/* links */
.links{height:540px}
.links .h2{left:0;right:0;top:72px;text-align:center}
.link-list{left:143px;top:136px;list-style:none}
.link-list li{height:38.4px;display:flex;align-items:center;gap:10px;font-size:16px;color:var(--sky)}
.links-photo{left:616px;top:144px;width:440px;height:318px;background:linear-gradient(120deg,#3f4650 0%,#7b838c 50%,#c9ced2 100%)}

/* about */
.about{height:520px;background:linear-gradient(90deg,#262080 0%,#2536a2 45%,#1e8fd8 100%)}
.about-photo{left:145px;top:20px;width:335px;height:500px;background:linear-gradient(180deg,#5a86b8 0%,#7aa7d4 55%,#8db5dc 100%)}
.about .h2{left:616px;top:104px;color:#fff}
.about-text{left:616px;top:160px;width:440px;font-size:15px;line-height:29px;color:#fff}
.about-btn{left:616px;top:374px}

/* contact */
.contact{height:484px}
.contact .h2{left:0;right:0;top:74px;text-align:center}
.contact-form{left:143px;top:150px;width:442px;display:grid;grid-template-columns:217px 217px;gap:8px}
.field{height:40px;border:1px solid #c9ccd4;font-size:11px;color:#777;padding:12px 14px;display:flex;justify-content:space-between;align-items:center}
.field.message{grid-column:1/3;height:109px;align-items:flex-start}
.submit{grid-column:1/2;width:95px;margin-top:9px}
.contact-info{left:632px;top:140px;list-style:none}
.contact-info li{height:48px;display:flex;align-items:center;gap:14px;font-size:19px;color:var(--navy)}

/* footer */
.site-footer{height:260px;background:var(--ink);color:#b8b6d8}
.footer-nav{left:143px;top:34px;font-size:11px}
.footer-copy{left:143px;top:66px;font-size:11px}
.footer-social{right:144px;top:52px;display:flex;gap:20px}
.footer-social span{width:16px;height:16px;border-radius:50%;background:#8c89c4}
.footer-rule{left:143px;top:112px;width:914px;height:1px;background:#3a3775}
.disclaimer{left:143px;top:128px;width:914px;font-size:9.5px;line-height:19px;color:#8d8ab8}
</style>
</head>
<body>

<header class="site-header">
  <div class="brand abs"><span class="brand-mark"></span><span class="brand-name">Mentorvale</span></div>
  <div class="header-phone abs">
    <svg width="20" height="20" viewBox="0 0 24 24"><path fill="#262080" d="M6.6 10.8a15 15 0 0 0 6.6 6.6l2.2-2.2c.3-.3.7-.4 1-.2 1.1.4 2.3.6 3.6.6.6 0 1 .4 1 1V20c0 .6-.4 1-1 1A17 17 0 0 1 3 4c0-.6.4-1 1-1h3.5c.6 0 1 .4 1 1 0 1.3.2 2.5.6 3.6.1.3 0 .7-.2 1z"/></svg>
    456 213 0190
  </div>
  <nav class="main-nav abs">
    <span class="is-active">Vision</span><span>Coaching</span><span>Support</span><span>Blog</span><span>Links</span><span>About me</span><span>Contact me</span>
  </nav>
</header>

<section class="hero">
  <div class="hero-photo abs" role="img" aria-label="Photo of a smiling coach in conversation with a client at an office table"></div>
  <div class="hero-copy abs">
    <div class="hero-title">Cras sollicitudin<br>cursus dui placerat</div>
    <span class="hero-cta">Book an appointment</span>
  </div>
  <span class="slider-arrow abs" style="left:46px"><svg width="16" height="16" viewBox="0 0 16 16"><path d="M10 3 5 8l5 5" stroke="#222" stroke-width="2.2" fill="none"/></svg></span>
  <span class="slider-arrow abs" style="left:1106px"><svg width="16" height="16" viewBox="0 0 16 16"><path d="m6 3 5 5-5 5" stroke="#222" stroke-width="2.2" fill="none"/></svg></span>
</section>

<section class="vision">
  <h2 class="h2 abs">Vision</h2>
  <div class="vision-rule abs"></div>
  <div class="vision-rule-active abs"></div>
  <div class="vision-split abs"></div>
  <div class="vision-tabs abs">
    <div class="vision-tab is-active">Why do I do this</div>
    <div class="vision-tab">How do I do this</div>
    <div class="vision-tab">What am I doing</div>
  </div>
  <p class="vision-text abs">Pellentesque a imperdiet dolor auctor est. Fusce sollicitudin lorem luctus volutpat. Proin placerat dapibus gravida. In tristique tristique nulla eget hendrerit. Maecenas vel tortor accumsan quam varius imperdiet vel eget elit. Aenean facilisis tincidunt lectus, id dictum nisi luctus eget. Vivamus efficitur ex condimentum, malesuada eros eget, feugiat nibh. Sed tellus ex, imperdiet eget gravida sit amet, volutpat eget turpis. In nec ultricies est. Etiam mattis augue vehicula odio posuere, sit amet tempus lectus luctus.</p>
  <svg class="vision-more abs" width="22" height="22" viewBox="0 0 22 22"><circle cx="11" cy="11" r="11" fill="#1ea7e1"/><path d="m9 6 5 5-5 5" stroke="#fff" stroke-width="2.4" fill="none"/></svg>
</section>

<section class="coaching">
  <div class="tile-grid abs">
    <div class="tile tile-title">Coaching</div>
    <div class="tile">
      <svg width="66" height="60" viewBox="0 0 66 60" fill="none" stroke="#222" stroke-width="2"><rect x="3" y="14" width="60" height="42" rx="3"/><path d="M24 14V6h18v8M3 30h60M29 27h8v7h-8z"/></svg>
      Career development
    </div>
    <div class="tile">
      <svg width="66" height="60" viewBox="0 0 66 60" fill="none" stroke="#222" stroke-width="2"><path d="M6 44 24 20l10 4 10-14M60 44 42 20l-10 4M22 34l10 10M28 30l10 10M34 26l10 10"/></svg>
      Conflicts
    </div>
    <div class="tile">
      <svg width="62" height="62" viewBox="0 0 62 62" fill="none" stroke="#222" stroke-width="2"><circle cx="31" cy="31" r="28"/><circle cx="31" cy="18" r="2" fill="#222"/><path d="M31 26v20"/></svg>
      What is coaching, why coaching
    </div>
    <div class="tile">
      <svg width="64" height="62" viewBox="0 0 64 62" fill="none" stroke="#222" stroke-width="2"><rect x="6" y="3" width="24" height="14"/><circle cx="20" cy="28" r="5"/><circle cx="42" cy="28" r="5"/><path d="M10 58V42c0-4 4-7 10-7s10 3 10 7v16M32 58V42c0-4 4-7 10-7s10 3 10 7v16"/></svg>
      Conduct of a session and of the whole consultation Limits of coaching
    </div>
    <div class="tile">
      <svg width="64" height="62" viewBox="0 0 64 62" fill="none" stroke="#222" stroke-width="2"><circle cx="20" cy="14" r="9"/><path d="M16 24v5h8v-5M38 58V44M46 58V36M54 58V28M36 24l20-18M50 6h6v6"/><circle cx="20" cy="40" r="5"/><path d="M10 58c0-6 4-10 10-10s10 4 10 10"/></svg>
      Examples of positive effects of coaching
    </div>
  </div>
</section>

<section class="support">
  <h2 class="h2 abs">Support</h2>
  <p class="support-text abs">Pellentesque a imperdiet dolor auctor est. Fusce sollicitudin lorem luctus volutpat. Proin placerat dapibus gravida. In tristique tristique nulla eget hendrerit. Maecenas vel tortor accumsan quam varius imperdiet vel eget elit. Aenean facilisis tincidunt lectus, id dictum nisi luctus eget. Vivamus efficitur ex condimentum, malesuada eros eget.</p>
  <span class="btn support-btn abs">Read more</span>
  <div class="support-art abs" role="img" aria-label="Illustration of stacked blue and navy cubes carrying support concept icons"></div>
</section>

<section class="blog">
  <h2 class="h2 abs">Blog</h2>
  <div class="blog-photo abs" role="img" aria-label="Photo of a team discussing ideas around a meeting table"></div>
  <article class="post abs" style="top:152px">
    <div class="post-date"><div class="post-day">23<span>JUN</span></div><div class="post-meta">by Mara Linde<br>Pellentesque convallis molestie enim</div></div>
    <h3 class="post-title">Fusce vitae lectus amet pulvinar maximus. Aenean placerat, nibh vel accumsan aliquet, magna nibh accumsan.</h3>
  </article>
  <article class="post abs" style="top:384px">
    <div class="post-date"><div class="post-day">23<span>JUN</span></div><div class="post-meta">by Mara Linde<br>Pellentesque convallis molestie enim</div></div>
    <h3 class="post-title">Proin a dolor mauris. Vestibulum ante ipsum primis in faucibus orci luctus et ultrices eget posuere cubilia.</h3>
  </article>
  <span class="btn blog-btn abs">View all</span>
</section>

<section class="links">
  <h2 class="h2 abs">Links</h2>
  <ul class="link-list abs">
    <li><svg width="12" height="12" viewBox="0 0 12 12"><circle cx="6" cy="6" r="6" fill="#1ea7e1"/><path d="m5 3 3 3-3 3" stroke="#fff" stroke-width="1.6" fill="none"/></svg>Etiam mattis augue vehicula odio posuere amet tempus</li>
    <li><svg width="12" height="12" viewBox="0 0 12 12"><circle cx="6" cy="6" r="6" fill="#1ea7e1"/><path d="m5 3 3 3-3 3" stroke="#fff" stroke-width="1.6" fill="none"/></svg>Cras sollicitudin cursus dui eu placerat</li>
    <li><svg width="12" height="12" viewBox="0 0 12 12"><circle cx="6" cy="6" r="6" fill="#1ea7e1"/><path d="m5 3 3 3-3 3" stroke="#fff" stroke-width="1.6" fill="none"/></svg>Aliquam erat volutpat</li>
    <li><svg width="12" height="12" viewBox="0 0 12 12"><circle cx="6" cy="6" r="6" fill="#1ea7e1"/><path d="m5 3 3 3-3 3" stroke="#fff" stroke-width="1.6" fill="none"/></svg>Pellentesque convallis molestie enim sit amet</li>
    <li><svg width="12" height="12" viewBox="0 0 12 12"><circle cx="6" cy="6" r="6" fill="#1ea7e1"/><path d="m5 3 3 3-3 3" stroke="#fff" stroke-width="1.6" fill="none"/></svg>Fusce vitae lectus sit amet mi pulvinar maximus</li>
    <li><svg width="12" height="12" viewBox="0 0 12 12"><circle cx="6" cy="6" r="6" fill="#1ea7e1"/><path d="m5 3 3 3-3 3" stroke="#fff" stroke-width="1.6" fill="none"/></svg>Cras augue magna, placerat eget nulla</li>
    <li><svg width="12" height="12" viewBox="0 0 12 12"><circle cx="6" cy="6" r="6" fill="#1ea7e1"/><path d="m5 3 3 3-3 3" stroke="#fff" stroke-width="1.6" fill="none"/></svg>Vestibulum ante ipsum primis in faucibus orci</li>
    <li><svg width="12" height="12" viewBox="0 0 12 12"><circle cx="6" cy="6" r="6" fill="#1ea7e1"/><path d="m5 3 3 3-3 3" stroke="#fff" stroke-width="1.6" fill="none"/></svg>Phasellus nisl est, condimentum vitae faucibus</li>
    <li><svg width="12" height="12" viewBox="0 0 12 12"><circle cx="6" cy="6" r="6" fill="#1ea7e1"/><path d="m5 3 3 3-3 3" stroke="#fff" stroke-width="1.6" fill="none"/></svg>Nunc sit amet consequat risus</li>
  </ul>
  <div class="links-photo abs" role="img" aria-label="Photo of two businessmen shaking hands across a desk"></div>
</section>

<section class="about">
  <div class="about-photo abs" role="img" aria-label="Portrait photo of the coach standing with arms crossed in a light blue shirt"></div>
  <h2 class="h2 abs">About me</h2>
  <p class="about-text abs">Pellentesque a imperdiet dolor auctor est. Fusce sollicitudin lorem luctus volutpat. Proin placerat dapibus gravida. In tristique tristique nulla eget hendrerit. Maecenas vel tortor accumsan quam varius imperdiet vel eget elit. Aenean facilisis tincidunt lectus, id dictum nisi luctus eget. Vivamus efficitur ex condimentum, malesuada eros eget.</p>
  <span class="btn about-btn abs">Read more</span>
</section>

<section class="contact">
  <h2 class="h2 abs">Contact us</h2>
  <div class="contact-form abs">
    <div class="field">Name</div>
    <div class="field">Email</div>
    <div class="field">Phone</div>
    <div class="field">Service for <svg width="10" height="8" viewBox="0 0 10 8"><path d="m1 2 4 4 4-4" stroke="#555" stroke-width="1.6" fill="none"/></svg></div>
    <div class="field message">Message</div>
    <span class="btn submit">Submit</span>
  </div>
  <ul class="contact-info abs">
    <li><svg width="14" height="18" viewBox="0 0 14 18"><path fill="#262080" d="M7 0a7 7 0 0 0-7 7c0 5 7 11 7 11s7-6 7-11a7 7 0 0 0-7-7zm0 10a3 3 0 1 1 0-6 3 3 0 0 1 0 6z"/></svg>24 Alder Court, Brookline Row, Westfield 40218</li>
    <li><svg width="16" height="16" viewBox="0 0 24 24"><path fill="#262080" d="M6.6 10.8a15 15 0 0 0 6.6 6.6l2.2-2.2c.3-.3.7-.4 1-.2 1.1.4 2.3.6 3.6.6.6 0 1 .4 1 1V20c0 .6-.4 1-1 1A17 17 0 0 1 3 4c0-.6.4-1 1-1h3.5c.6 0 1 .4 1 1 0 1.3.2 2.5.6 3.6.1.3 0 .7-.2 1z"/></svg>Phone : 546 132 0175</li>
    <li><svg width="16" height="13" viewBox="0 0 16 13"><rect width="16" height="13" rx="1.5" fill="#262080"/><path d="m1 2 7 5 7-5" stroke="#fff" stroke-width="1.3" fill="none"/></svg>Email : hello@mentorvale.com</li>
  </ul>
</section>

<footer class="site-footer">
  <div class="footer-nav abs">Vision &nbsp;|&nbsp; Coaching &nbsp;|&nbsp; Support &nbsp;|&nbsp; Blog &nbsp;|&nbsp; Links &nbsp;|&nbsp; About Me &nbsp;|&nbsp; Contact Me</div>
  <div class="footer-copy abs">Copyright © 2020 Mentorvale. All rights reserved.</div>
  <div class="footer-social abs"><span></span><span></span></div>
  <div class="footer-rule abs"></div>
  <p class="disclaimer abs">Disclaimer : The content on this site is provided for general information only and does not replace individual professional advice. Coaching sessions support personal and team development but are not a substitute for medical, legal or therapeutic care. Results depend on each client and cannot be guaranteed. Mentorvale takes no responsibility for external links or the content of third party pages referenced here. All texts and images remain the property of their owners and may not be reused without written permission. Personal data sent through the contact form is handled with care and used only to answer your request. For questions about privacy or these terms, please reach out using the contact details above.</p>
</footer>

</body>
</html>
```